Business Card and Stationary Designs for commercial construction company
Halvern Builders, Inc.
Creative Brief
Use standard fonts
Dennis Whitlock
Director of Operations
6387 Larkmeadow Lane Pinecrest Falls, NV 95731
dennis.whitlock@halvernbldg.com
License #3084519
We like the colors of our logo, so please incorporate them into the card. The font for the other information on the business card does not have to match the logo font, but it should coordinate with it. We need the stationary design to be used to print actual stationary, but we would also like a word document that we can use for creating letters on electronic stationary.

```html
<!DOCTYPE html>
<html lang="en">
<head>
<meta charset="utf-8">
<title>Halvern Builders, Inc. – Business Card</title>
<link href="https://fonts.googleapis.com/css2?family=Open+Sans:wght@400;600;800&display=swap" rel="stylesheet">
<style>
  :root {
    --bg: #6e6e6e;
    --red: #e0242c;
    --red-dark: #b5161d;
    --red-light: #ef3a40;
    --white: #ffffff;
    --grey: #8a8a8a;
    --ink: #3b3b3b;
  }
  * { margin: 0; padding: 0; box-sizing: border-box; }
  html, body { width: 1200px; height: 908px; overflow: hidden; }
  body {
    background: var(--bg);
    font-family: "Open Sans", Arial, sans-serif;
    display: flex;
    flex-direction: column;
    align-items: center;
    justify-content: center;
    gap: 36px;
  }
  .card {
    width: 700px;
    height: 400px;
    border-radius: 22px;
    overflow: hidden;
    position: relative;
    box-shadow: 0 10px 24px rgba(0,0,0,.35);
  }
  /* Front */
  .card-front {
    background: linear-gradient(135deg, var(--red-light) 0%, var(--red) 55%, var(--red-dark) 100%);
  }
  .card-front .wordmark {
    position: absolute;
    left: 64px;
    top: 212px;
  }
  .wordmark {
    display: flex;
    align-items: center;
    gap: 14px;
  }
  .wordmark-square {
    width: 30px; height: 30px;
    background: var(--white);
  }
  .wordmark-name {
    font-weight: 800;
    font-size: 40px;
    letter-spacing: 1px;
    line-height: 1;
    color: var(--white);
  }
  /* Back */
  .card-back { background: var(--white); }
  .back-shape { position: absolute; inset: 0; }
  .back-info {
    position: absolute;
    left: 48px;
    top: 52px;
  }
  .back-info .wordmark-square { background: var(--red); width: 26px; height: 26px; }
  .back-info .wordmark-name { color: var(--red); font-size: 34px; }
  .contact { margin-top: 34px; font-size: 15px; line-height: 1.55; color: var(--ink); }
  .license { color: var(--red); font-weight: 600; }
  .contact-line { display: flex; align-items: center; gap: 8px; }
  .icon {
    width: 16px; height: 16px; border-radius: 50%;
    background: var(--red);
    display: inline-flex; align-items: center; justify-content: center;
    flex: none;
  }
  .person {
    position: absolute;
    right: 44px;
    top: 150px;
    text-align: right;
    color: var(--white);
  }
  .person-name { font-size: 24px; font-weight: 600; line-height: 1.3; }
  .person-title { font-size: 16px; }
</style>
</head>
<body>
  <section class="card card-front">
    <div class="wordmark">
      <span class="wordmark-square"></span>
      <span class="wordmark-name">HALVERN BUILDERS</span>
    </div>
  </section>

  <section class="card card-back">
    <svg class="back-shape" viewBox="0 0 700 400" preserveAspectRatio="none">
      <path d="M420 0 C 360 120, 380 300, 470 400 L700 400 L700 0 Z" fill="#8a8a8a"/>
      <path d="M440 0 C 385 120, 405 300, 495 400 L700 400 L700 0 Z" fill="#e0242c"/>
    </svg>

    <div class="back-info">
      <div class="wordmark">
        <span class="wordmark-square"></span>
        <span class="wordmark-name">HALVERN</span>
      </div>
      <div class="contact">
        <p class="license">License #3084519</p>
        <p>6387 Larkmeadow Lane</p>
        <p>Pinecrest Falls, NV 95731</p>
        <p class="contact-line"><span class="icon"><svg width="9" height="9" viewBox="0 0 24 24"><path fill="#fff" d="M6.6 10.8a15 15 0 0 0 6.6 6.6l2.2-2.2c.3-.3.7-.4 1-.2 1.1.4 2.3.6 3.6.6.6 0 1 .4 1 1V20c0 .6-.4 1-1 1A17 17 0 0 1 3 4c0-.6.4-1 1-1h3.5c.6 0 1 .4 1 1 0 1.3.2 2.5.6 3.6.1.3 0 .7-.2 1z"/></svg></span>530-555-0182</p>
        <p class="contact-line"><span class="icon"><svg width="9" height="9" viewBox="0 0 24 24"><path fill="#fff" d="M6.6 10.8a15 15 0 0 0 6.6 6.6l2.2-2.2c.3-.3.7-.4 1-.2 1.1.4 2.3.6 3.6.6.6 0 1 .4 1 1V20c0 .6-.4 1-1 1A17 17 0 0 1 3 4c0-.6.4-1 1-1h3.5c.6 0 1 .4 1 1 0 1.3.2 2.5.6 3.6.1.3 0 .7-.2 1z"/></svg></span>530-555-0147</p>
        <p class="contact-line"><span class="icon"><svg width="9" height="9" viewBox="0 0 24 24"><rect x="4" y="3" width="16" height="18" rx="2" fill="#fff"/></svg></span>530-555-0193</p>
        <p class="contact-line"><span class="icon"><svg width="9" height="9" viewBox="0 0 24 24"><rect x="2" y="5" width="20" height="14" fill="#fff"/><path d="M2 5l10 8 10-8" fill="none" stroke="#e0242c" stroke-width="2"/></svg></span>dennis.whitlock@halvernbldg.com</p>
      </div>
    </div>

    <div class="person">
      <p class="person-name">Dennis Whitlock</p>
      <p class="person-title">Director of Operations</p>
    </div>
  </section>
</body>
</html>
```